Power/Telecommunications Contracting Ad

We need an eye catching advertisement that will be posted in magazines and news papers. I am open to all sizes of ad space. It has to have a list of things we do, our contact info and a logo of Velm Accreditation.
We provide:
Telecommunications and High/Low voltage Power Construction
Horizontal Directional Drilling (Trenchless conduit installation)
Vibratory Cable Plowing
Trenching/Excavating for underground utilities
Telecommunications cable splicing
Pole installation and overhead aerial construction
Underground power and telecom cable Installations
Snowcat Services
Located at:
58 Fenwick Lane
Whitehorse Yukon Canada
Y2B 7K9

Contact:
Morris Caskey
President
Morris@brindlenet.example
(867)555-0192

Lionel Caskey
Vice President
Lionel@brindlenet.example
(867)555-0147

Target Market(s)

New clients

Industry/Entity Type

Telecommunications

Requirements
Must have
• Contact info, address, list of services, for certification logo
Nice to have
• I've attatched some pictures of the work we do if you could try to incorporate them into the ad that would be good.

```html
<!DOCTYPE html>
<html lang="en">
<head>
<meta charset="utf-8">
<title>Power &amp; Telecommunications Contracting Ad</title>
<link href="https://fonts.googleapis.com/css2?family=Lato:wght@400;700;900&family=Montserrat:wght@500;700;800&display=swap" rel="stylesheet">
<style>
  :root {
    --stage: #e4e4e4;
    --ink: #262626;
    --gold: #f5bd1f;
    --paper: #ffffff;
    --text-light: #ffffff;
  }
  * { box-sizing: border-box; margin: 0; padding: 0; }
  html, body { width: 1200px; height: 1200px; overflow: hidden; }
  body {
    background: var(--stage);
    font-family: "Lato", Arial, sans-serif;
    position: relative;
  }
  .ad {
    position: absolute;
    left: 210px; top: 50px;
    width: 780px; height: 1100px;
    background: var(--ink);
    overflow: hidden;
    box-shadow: 0 12px 30px rgba(0,0,0,.25);
  }
  .ad-shapes { position: absolute; inset: 0; }
  .brand {
    position: absolute;
    left: 540px; top: 120px; width: 230px;
    display: flex; align-items: center; gap: 10px;
  }
  .brand-dot { width: 22px; height: 22px; border-radius: 50%; background: var(--ink); flex: none; }
  .brand-name {
    font-family: "Lato", Arial, sans-serif;
    font-weight: 900; font-size: 30px; line-height: 1.05;
    color: var(--ink);
  }
  .services {
    position: absolute;
    left: 538px; top: 305px; width: 232px;
    color: var(--text-light);
  }
  .services-title {
    font-family: "Lato", Arial, sans-serif;
    font-weight: 900; font-size: 21px;
    color: var(--gold);
    margin-bottom: 14px;
  }
  .services-list { list-style: none; }
  .services-list li {
    position: relative;
    padding-left: 20px;
    font-size: 14.5px; line-height: 1.25;
    margin-bottom: 12px;
  }
  .services-list li::before {
    content: ""; position: absolute;
    left: 2px; top: 6px;
    width: 8px; height: 8px; border-radius: 50%;
    background: var(--gold);
  }
  .contact {
    position: absolute;
    left: 0; top: 795px; width: 575px; height: 195px;
    color: var(--ink);
  }
  .contact-title {
    position: absolute; left: 220px; top: 8px;
    font-family: "Montserrat", Arial, sans-serif;
    font-weight: 800; font-size: 24px; letter-spacing: 1px;
    border-bottom: 2px solid var(--ink);
    padding-bottom: 2px;
  }
  .contact-divider {
    position: absolute; left: 330px; top: 55px;
    width: 2px; height: 120px; background: var(--ink);
  }
  .person { position: absolute; }
  .person-lead { left: 40px; top: 70px; }
  .person-vice { left: 350px; top: 45px; }
  .person-name {
    display: inline-block;
    background: var(--ink); color: var(--text-light);
    font-family: "Montserrat", Arial, sans-serif;
    font-weight: 700; font-size: 16px;
    padding: 5px 10px;
  }
  .person-role { font-family: "Montserrat", Arial, sans-serif; font-size: 18px; margin-top: 6px; }
  .person-line { display: flex; align-items: center; gap: 6px; margin-top: 3px; white-space: nowrap; }
  .person-line.email { font-family: "Montserrat", Arial, sans-serif; font-size: 13px; color: var(--paper); }
  .person-line.phone { font-family: "Montserrat", Arial, sans-serif; font-weight: 700; font-size: 17px; }
  .person-line svg { width: 12px; height: 12px; flex: none; }
  .location {
    position: absolute;
    left: 0; top: 990px; width: 575px; height: 65px;
    background: var(--paper);
    padding: 10px 0 0 40px;
  }
  .location-label {
    display: inline-block;
    background: var(--ink); color: var(--gold);
    font-family: "Montserrat", Arial, sans-serif;
    font-weight: 800; font-size: 17px;
    padding: 3px 10px;
  }
  .location-address {
    position: absolute; left: 178px; top: 16px;
    font-weight: 700; font-size: 13px; color: var(--ink);
    white-space: nowrap;
  }
  .website {
    position: absolute; left: 40px; top: 1068px;
    font-family: "Montserrat", Arial, sans-serif;
    font-weight: 700; font-size: 15px; letter-spacing: 4px;
    color: var(--gold);
  }
  .snowcat-photo {
    position: absolute;
    left: 585px; top: 925px; width: 195px; height: 175px;
    background: linear-gradient(160deg, #dfe6ec 0%, #c9332a 45%, #8d1f1a 70%, #e9edf0 100%);
  }
</style>
</head>
<body>
  <main class="ad">
    <svg class="ad-shapes" viewBox="0 0 780 1100" width="780" height="1100">
      <defs>
        <linearGradient id="work-photo-tones" x1="0" y1="0" x2="0" y2="1">
          <stop offset="0" stop-color="#c9d2db"/>
          <stop offset="0.35" stop-color="#7c6f64"/>
          <stop offset="0.6" stop-color="#e7ecf0"/>
          <stop offset="1" stop-color="#f2f4f6"/>
        </linearGradient>
      </defs>
      <polygon points="330,0 780,0 780,215 520,265 520,200" fill="var(--gold)"/>
      <polygon role="img" aria-label="Photo of a lineman in safety gear climbing a wooden power pole above a snowy equipment yard"
               points="0,0 330,0 520,200 520,800 0,800" fill="url(#work-photo-tones)"/>
      <polygon points="650,790 700,790 670,880 620,880" fill="var(--gold)"/>
      <polygon points="720,790 760,790 730,880 690,880" fill="var(--gold)"/>
      <polygon points="0,800 600,770 575,990 0,990" fill="var(--gold)"/>
    </svg>

    <div class="brand">
      <span class="brand-dot"></span>
      <span class="brand-name">Velm Accreditation</span>
    </div>

    <section class="services">
      <h2 class="services-title">SERVICES WE OFFER :</h2>
      <ul class="services-list">
        <li>Telecommunications and High/Low voltage Power Construction</li>
        <li>Horizontal Directional Drilling (Trenchless conduit installation)</li>
        <li>Vibratory Cable Plowing</li>
        <li>Trenching/Excavating for underground utilities</li>
        <li>Telecommunications cable splicing</li>
        <li>Pole installation and overhead aerial construction</li>
        <li>Underground power and telecom cable Installations</li>
        <li>Snowcat Services</li>
      </ul>
    </section>

    <section class="contact">
      <h2 class="contact-title">CONTACT:</h2>
      <div class="contact-divider"></div>
      <div class="person person-lead">
        <div class="person-name">Morris Caskey</div>
        <div class="person-role">President</div>
        <div class="person-line email">
          <svg viewBox="0 0 12 12"><rect x="0.5" y="2" width="11" height="8" fill="var(--ink)"/><path d="M0.5 2 L6 7 L11.5 2" stroke="var(--gold)" fill="none"/></svg>
          Morris@brindlenet.example
        </div>
        <div class="person-line phone">
          <svg viewBox="0 0 12 12"><path d="M2 1 L4.5 1 L5 4 L3.5 5 Q5 8 7 8.5 L8 7 L11 7.5 L11 10 Q6 11.5 2 6 Q0.5 3 2 1Z" fill="var(--ink)"/></svg>
          (867)555-0192
        </div>
      </div>
      <div class="person person-vice">
        <div class="person-name">Lionel Caskey</div>
        <div class="person-role">Vice President</div>
        <div class="person-line email">
          <svg viewBox="0 0 12 12"><rect x="0.5" y="2" width="11" height="8" fill="var(--ink)"/><path d="M0.5 2 L6 7 L11.5 2" stroke="var(--gold)" fill="none"/></svg>
          Lionel@brindlenet.example
        </div>
        <div class="person-line phone">
          <svg viewBox="0 0 12 12"><path d="M2 1 L4.5 1 L5 4 L3.5 5 Q5 8 7 8.5 L8 7 L11 7.5 L11 10 Q6 11.5 2 6 Q0.5 3 2 1Z" fill="var(--ink)"/></svg>
          (867)555-0147
        </div>
      </div>
    </section>

    <section class="location">
      <span class="location-label">LOCATION :</span>
      <p class="location-address">58 Fenwick Lane Whitehorse Yukon Canada Y2B 7K9</p>
    </section>

    <p class="website">www.brindlelines.example</p>

    <div class="snowcat-photo" role="img" aria-label="Photo of a red tracked snowcat vehicle parked in the snow beside a building"></div>
  </main>
</body>
</html>
```